company name - HARLOWMERE AIRPORT TRANSFER.
include this information please .....25 YEARS EXPERIENCE / CARS+MPVS+MINIBUSES AVAILABLE - ALL AT SAME PRICE AT ANY TIME OF DAY. NO EXTRA HIDDEN CHARGES.

PRICES [ selection ] ......

BRAXMOOR ....£100
CORVALE ....£130
DERRIN...£55.00
QUILLBOURNE ...£60.00
HALVERSTOKE ...£100.00
UPPER KESTLING ...£100,00
QUAYSIDE AIRPORT ...£95.00

```html
<!DOCTYPE html>
<html lang="en">
<head>
<meta charset="utf-8">
<title>Harlowmere Airport Transfer</title>
<link rel="stylesheet" href="https://fonts.googleapis.com/css2?family=Montserrat:wght@500;700;800;900&display=swap">
<style>
  :root {
    --sky-deep: #1266c4;
    --sky-mid: #2a95e3;
    --sky-light: #cdeafa;
    --navy: #1e3a8a;
    --brand-blue: #1b8fdc;
    --ink: #0b0b0b;
    --white: #ffffff;
  }
  * { margin: 0; padding: 0; box-sizing: border-box; }
  html, body { width: 852px; height: 1200px; overflow: hidden; background: var(--white); }
  body { font-family: "Montserrat", Arial, sans-serif; }

  .flyer { position: relative; width: 852px; height: 1200px; overflow: hidden; }
  .backdrop { position: absolute; inset: 0; }

  .brand {
    position: absolute; top: 78px; left: 0; width: 852px;
    text-align: center; color: var(--white);
    font-weight: 800; font-size: 56px; line-height: 1.08; letter-spacing: 1px;
  }

  .intro { position: absolute; top: 350px; left: 0; width: 852px; text-align: center; color: var(--ink); }
  .intro__headline { font-weight: 900; font-size: 50px; letter-spacing: 0.5px; line-height: 1.1; }
  .intro__lines { font-weight: 700; font-size: 28px; line-height: 1.2; margin-top: 4px; }
  .intro__note { font-weight: 500; font-size: 22px; margin-top: 4px; }

  .fleet { position: absolute; top: 510px; left: 100px; width: 670px; height: 120px; display: flex; gap: 22px; align-items: flex-end; }
  .fleet__vehicle { flex: 1; border-radius: 40px 40px 14px 14px; background: linear-gradient(180deg, #e9eef3 0%, #aab4be 100%); }
  .fleet__vehicle--car { height: 100px; }
  .fleet__vehicle--mpv { height: 108px; }
  .fleet__vehicle--bus { height: 120px; border-radius: 18px 30px 12px 12px; background: linear-gradient(180deg, #ffffff 0%, #c7ced6 100%); }

  .prices {
    position: absolute; top: 640px; left: 70px; width: 706px; height: 350px;
    background: var(--white); border-radius: 34px;
    border: 8px solid var(--sky-mid);
    padding: 28px 90px 0 88px; list-style: none;
  }
  .prices__row { display: flex; align-items: baseline; font-size: 29px; font-weight: 800; height: 42px; }
  .prices__place { color: var(--brand-blue); white-space: nowrap; }
  .prices__leader { flex: 1; border-bottom: 4px dotted var(--ink); margin: 0 8px; transform: translateY(-6px); }
  .prices__amount { color: var(--ink); font-weight: 700; white-space: nowrap; }

  .contact {
    position: absolute; top: 1036px; left: 520px;
    color: var(--brand-blue); font-weight: 800; font-size: 28px;
  }
  .jet { position: absolute; background: var(--white); border-radius: 50%; opacity: 0.9; }
  .jet--one { left: 258px; top: 1124px; width: 56px; height: 26px; }
  .jet--two { left: 448px; top: 1110px; width: 56px; height: 26px; background: var(--navy); }
</style>
</head>
<body>
<main class="flyer">
  <svg class="backdrop" width="852" height="1200" viewBox="0 0 852 1200" aria-hidden="true">
    <defs>
      <linearGradient id="skyGrad" x1="0" y1="0" x2="0" y2="1">
        <stop offset="0" stop-color="#1f8fe6"/>
        <stop offset="0.35" stop-color="#3fb1ef"/>
        <stop offset="0.5" stop-color="#d4eefb"/>
        <stop offset="0.7" stop-color="#3aa6ea"/>
        <stop offset="1" stop-color="#1266c4"/>
      </linearGradient>
      <linearGradient id="swoopGrad" x1="0" y1="0" x2="1" y2="0">
        <stop offset="0" stop-color="#1266c4"/>
        <stop offset="1" stop-color="#2a95e3"/>
      </linearGradient>
    </defs>
    <rect width="852" height="1200" fill="url(#skyGrad)"/>
    <path d="M0 0 H852 V170 C700 320 300 340 0 250 Z" fill="url(#swoopGrad)" opacity="0.85"/>
    <path d="M120 60 C300 -20 700 -10 852 40 V120 C650 40 320 60 120 60 Z" fill="#5cc4f3" opacity="0.5"/>
    <path d="M600 260 C720 320 820 420 852 600 V1000 C820 800 760 560 600 260 Z" fill="#1266c4" opacity="0.35"/>
    <path d="M0 1010 C250 1080 560 1000 852 940 V1200 H0 Z" fill="#ffffff"/>
    <path d="M0 1120 C260 1160 560 1100 852 1060 V1200 H0 Z" fill="#2a95e3" opacity="0.5"/>
    <path d="M0 1150 C280 1180 560 1130 852 1110 V1200 H0 Z" fill="#1e3a8a"/>
  </svg>

  <h1 class="brand">HARLOWMERE<br>AIRPORT TRANSFER</h1>

  <section class="intro">
    <h2 class="intro__headline">25 YEARS EXPERIENCE</h2>
    <p class="intro__lines">Cars+MPVs+Minibuses available.<br>All at same price at any time of day.</p>
    <p class="intro__note">No extra hidden charges.</p>
  </section>

  <div class="fleet">
    <div class="fleet__vehicle fleet__vehicle--car" role="img" aria-label="Photo of a silver hatchback car"></div>
    <div class="fleet__vehicle fleet__vehicle--mpv" role="img" aria-label="Photo of a silver MPV"></div>
    <div class="fleet__vehicle fleet__vehicle--bus" role="img" aria-label="Photo of a white minibus"></div>
  </div>

  <ul class="prices">
    <li class="prices__row"><span class="prices__place">BRAXMOOR</span><span class="prices__leader"></span><span class="prices__amount">£100</span></li>
    <li class="prices__row"><span class="prices__place">CORVALE</span><span class="prices__leader"></span><span class="prices__amount">£130</span></li>
    <li class="prices__row"><span class="prices__place">DERRIN</span><span class="prices__leader"></span><span class="prices__amount">£55.00</span></li>
    <li class="prices__row"><span class="prices__place">QUILLBOURNE</span><span class="prices__leader"></span><span class="prices__amount">£60.00</span></li>
    <li class="prices__row"><span class="prices__place">HALVERSTOKE</span><span class="prices__leader"></span><span class="prices__amount">£100.00</span></li>
    <li class="prices__row"><span class="prices__place">UPPER KESTLING</span><span class="prices__leader"></span><span class="prices__amount">£100,00</span></li>
    <li class="prices__row"><span class="prices__place">QUAYSIDE AIRPORT</span><span class="prices__leader"></span><span class="prices__amount">£95.00</span></li>
  </ul>

  <p class="contact">Phone details</p>

  <div class="jet jet--one" role="img" aria-label="Small white aeroplane silhouette"></div>
  <div class="jet jet--two" role="img" aria-label="Small navy aeroplane silhouette"></div>
</main>
</body>
</html>
```